Bright Harbour Mortgages Social Media Campaign

I need social media campaign banners. Facebook and Instagram.
I would like them to incorporate local photos, my photo and my logo. I have some sample files of previous campaigns and I have a color scheme associated with my brand. My business operates in St. John's Newfoundland.

Target Market(s)

Home Buyers, Home Owners

Industry/Entity Type

Mortgage Brokering

Logo Text

Bright Harbour Mortgages

Logo styles of interest
Lettermark Logo
Font styles to use
Other font styles liked:
• Times New Roman, I'm open to suggestion

Colors
0054AA
0677BA
7BADD7
CADEEF
E8F1F8
EE7325
F08F49
F5BC92
FAE3D3
FDF4ED

Requirements
Must have
• My name, photo, contact info, slogan
Nice to have
• We can discuss slogans to use, I can provide some suggestions.

```html
<!DOCTYPE html>
<html lang="en">
<head>
<meta charset="utf-8">
<title>Bright Harbour Mortgages – Social Banner</title>
<link rel="stylesheet" href="https://fonts.googleapis.com/css2?family=Montserrat:wght@400;500;600;700;800&display=swap">
<style>
  :root {
    --navy: #0b1a52;
    --navy-deep: #081545;
    --orange: #fa4a0c;
    --white: #ffffff;
    --sky-light: #a9cdf7;
    --sky: #3f8cf0;
    --sky-deep: #0b5fd6;
    --button-blue: #4c9ff5;
    --ring: #8ea8d6;
  }
  * { margin: 0; padding: 0; box-sizing: border-box; }
  html, body { width: 1200px; height: 1200px; overflow: hidden; background: var(--white); }
  body { font-family: "Montserrat", sans-serif; }
  .banner { position: relative; width: 1200px; height: 1200px; overflow: hidden; }
  .backdrop { position: absolute; inset: 0; }

  .brand { position: absolute; left: 52px; top: 222px; width: 500px; text-align: center; }
  .brand-name { font-weight: 800; font-size: 27px; color: var(--orange); white-space: nowrap; line-height: 1; }
  .brand-tagline { display: flex; align-items: center; justify-content: center; gap: 14px; margin-top: 12px;
    font-weight: 700; font-size: 15px; letter-spacing: 3px; color: var(--navy); white-space: nowrap; }
  .brand-tagline::before, .brand-tagline::after { content: ""; width: 52px; height: 2px; background: var(--navy); }

  .headline { position: absolute; left: 75px; top: 814px; color: var(--white); font-weight: 500; }
  .headline .line { display: block; white-space: nowrap; }
  .headline .line-1 { font-size: 40px; line-height: 54px; }
  .headline .line-2 { font-size: 40px; line-height: 62px; }
  .headline .line-3 { font-size: 40px; line-height: 58px; }
  .headline .accent { color: var(--orange); font-weight: 700; }
  .headline .accent-lg { font-size: 58px; }
  .headline .accent-md { font-size: 31px; }

  .divider { position: absolute; left: 75px; top: 995px; width: 590px; height: 2px; background: var(--white); }
  .subtext { position: absolute; left: 75px; top: 1008px; font-size: 21px; line-height: 32px; color: var(--white); font-weight: 500; }
  .subtext .accent { color: var(--orange); font-weight: 700; }

  .website { position: absolute; left: 78px; top: 1141px; display: flex; align-items: center; gap: 14px;
    font-size: 29px; font-weight: 500; color: var(--navy); }
  .website .accent { color: var(--orange); }

  .cta-button { position: absolute; left: 963px; top: 1047px; width: 199px; height: 44px; border-radius: 4px;
    background: var(--button-blue); color: var(--white); font-size: 24px; font-weight: 500;
    display: flex; align-items: center; justify-content: center; gap: 4px; }

  .contact { position: absolute; left: 747px; top: 1090px; color: var(--white); }
  .contact-label { font-size: 28px; font-weight: 700; line-height: 34px; }
  .contact-phone { display: flex; align-items: center; gap: 14px; font-size: 45px; font-weight: 800; line-height: 56px; }
</style>
</head>
<body>
<main class="banner">
  <svg class="backdrop" width="1200" height="1200" viewBox="0 0 1200 1200">
    <defs>
      <radialGradient id="sky" cx="0.28" cy="0" r="1.1">
        <stop offset="0" stop-color="var(--sky-light)"/>
        <stop offset="0.45" stop-color="var(--sky)"/>
        <stop offset="1" stop-color="var(--sky-deep)"/>
      </radialGradient>
      <linearGradient id="tower" x1="0" y1="0" x2="0" y2="1">
        <stop offset="0" stop-color="#5d8fd8"/>
        <stop offset="0.4" stop-color="#8a8a86"/>
        <stop offset="1" stop-color="#74655d"/>
      </linearGradient>
      <linearGradient id="portrait" x1="0" y1="0" x2="0" y2="1">
        <stop offset="0" stop-color="#c98a55"/>
        <stop offset="0.45" stop-color="#e2b59a"/>
        <stop offset="0.7" stop-color="#1c2a5a"/>
        <stop offset="1" stop-color="#142050"/>
      </linearGradient>
      <linearGradient id="keys" x1="0" y1="0" x2="1" y2="1">
        <stop offset="0" stop-color="#f2f2f4"/>
        <stop offset="0.6" stop-color="#e8c9b4"/>
        <stop offset="1" stop-color="#c99c82"/>
      </linearGradient>
    </defs>

    <rect class="sky-photo" width="1200" height="1200" fill="url(#sky)" role="img" aria-label="Photo of blue sky over St. John's"/>
    <rect class="tower-photo" x="660" y="60" width="540" height="800"
          fill="url(#tower)" role="img" aria-label="Photo of a historic stone signal tower on a hilltop"/>

    <polygon class="chevron-white" fill="var(--white)" points="0,710 568,386 1060,664 1200,584 1200,1200 0,1200"/>
    <polygon class="chevron-orange" fill="var(--orange)" points="0,729 568,405 1060,683 1200,603 1200,1200 0,1200"/>
    <polygon class="chevron-navy" fill="var(--navy-deep)" points="0,851 568,530 1068,812 1200,737 1200,1200 0,1200"/>

    <circle class="photo-ring" cx="257" cy="596" r="186" fill="var(--ring)" opacity="0.75"/>
    <circle class="keys-photo" cx="257" cy="596" r="167" fill="url(#keys)" role="img" aria-label="Photo of hands holding a model house and keys"/>

    <path class="advisor-photo" d="M700 1068 L720 880 C735 760 760 620 820 520 C860 440 920 402 1000 398 C1080 402 1140 440 1170 520 C1200 600 1200 700 1200 760 L1200 1068 Z"
          fill="url(#portrait)" role="img" aria-label="Portrait photo of the mortgage advisor"/>

    <rect class="web-bar" x="0" y="1121" width="700" height="79" fill="var(--white)"/>
    <polygon class="call-panel" fill="var(--orange)" points="640,1200 730,1068 1200,1068 1200,1200"/>
  </svg>

  <div class="brand">
    <div class="brand-name">BRIGHT HARBOUR MORTGAGES</div>
    <div class="brand-tagline">WE THINK OUTSIDE THE BOX</div>
  </div>

  <h1 class="headline">
    <span class="line line-1">Get The Keys</span>
    <span class="line line-2">To Your <span class="accent accent-lg">Dream Home</span></span>
    <span class="line line-3">With <span class="accent accent-md">Bright Harbour Mortgages!</span></span>
  </h1>
  <div class="divider"></div>
  <p class="subtext">Let Us I Help You Unlock Your <span class="accent">Dream Home Today</span><br>With Low Rates &amp; Great Deals!</p>

  <div class="website">
    <svg width="44" height="44" viewBox="0 0 44 44" aria-hidden="true">
      <circle cx="22" cy="22" r="20" fill="none" stroke="var(--navy)" stroke-width="2.5"/>
      <circle cx="22" cy="22" r="13" fill="var(--orange)"/>
      <g fill="none" stroke="var(--white)" stroke-width="1.4">
        <ellipse cx="22" cy="22" rx="5.5" ry="13"/>
        <line x1="9" y1="22" x2="35" y2="22"/>
        <line x1="11" y1="15" x2="33" y2="15"/>
        <line x1="11" y1="29" x2="33" y2="29"/>
      </g>
    </svg>
    <span>www.<span class="accent">harbourlightmortgages</span>.com</span>
  </div>

  <div class="cta-button">Get Started
    <svg width="24" height="22" viewBox="0 0 24 22" aria-hidden="true">
      <path d="M3 3 L11 11 L3 19 M12 3 L20 11 L12 19" fill="none" stroke="var(--white)" stroke-width="4"/>
    </svg>
  </div>

  <div class="contact">
    <div class="contact-label">Call Maren:</div>
    <div class="contact-phone">
      <svg width="34" height="34" viewBox="0 0 24 24" aria-hidden="true">
        <path fill="var(--white)" d="M6.6 10.8c1.4 2.8 3.8 5.1 6.6 6.6l2.2-2.2c.3-.3.7-.4 1-.2 1.1.4 2.3.6 3.6.6.6 0 1 .4 1 1V20c0 .6-.4 1-1 1C10.6 21 3 13.4 3 4c0-.6.4-1 1-1h3.5c.6 0 1 .4 1 1 0 1.3.2 2.5.6 3.6.1.3 0 .7-.2 1z"/>
        <path fill="none" stroke="var(--white)" stroke-width="1.8" d="M14 3a7 7 0 0 1 7 7 M14 6.5a3.5 3.5 0 0 1 3.5 3.5"/>
      </svg>
      <span>709-555-0142</span>
    </div>
  </div>
</main>
</body>
</html>
```